Mediation service showing compassion, collaboration, and resolution

I would like to purchase a customized version of a design you have previously submitted - https://www.pixelbidhub.com/design/48172635

Hello,

I would like a design for a flyer for my mediation business.
I also want to include a message that says that I offer rates on sliding scale.
My website is: www.morvantelkresolve.com

Let me know what other details you might want?

Thank you,

Teodric

Target Market(s)

Local community, western Massachusetts USA. Businesses, families, individuals.

Industry/Entity Type

Mediation, Legal, Alternative Dispute Resolution, Divorce, Unions

Font styles to use
Sans Serif

Colors
0094D4
00A9DD
6FCCEA
C7EBF8
E9F6FB
00AB8E
00BBA5
67D7C9
C6EFE9
E9F9F6

Requirements
Must have
• “Sliding scale rates available “. Phone and email details. +1.555.384.7290 and email: teodric@morvantelkresolve.com as well as we code to my website www.morvantelkresolve.com

```html
<!DOCTYPE html>
<html lang="en">
<head>
<meta charset="utf-8">
<title>Teodric F. Morvantelk — Mediation Flyer</title>
<link href="https://fonts.googleapis.com/css2?family=Bebas+Neue&family=Josefin+Sans:wght@600;700&family=Montserrat:wght@500&family=EB+Garamond&display=swap" rel="stylesheet">
<style>
  :root {
    --sky-blue: #16a8db;
    --seafoam: #8dd9d1;
    --mist: #e8e8ec;
    --ink: #111111;
    --white: #ffffff;
    --footer-ink: #4a4a4a;
    --gold: #b39a4f;
    --olive: #8c8a3e;
    --circle-blue: #7fa6d6;
  }
  html, body { margin: 0; padding: 0; overflow: hidden; }
  body { width: 900px; height: 1200px; background: var(--white); }
  .flyer { position: relative; width: 900px; height: 1200px; overflow: hidden; background: var(--white); }

  .hero-photo {
    position: absolute; left: 0; top: 0; width: 900px; height: 1093px;
    background:
      radial-gradient(ellipse 300px 200px at 470px 860px, #e8b9a1 0%, rgba(232,185,161,0.55) 45%, rgba(232,232,236,0) 100%),
      radial-gradient(ellipse 260px 110px at 230px 640px, #e2b096 0%, rgba(226,176,150,0) 100%),
      radial-gradient(ellipse 200px 120px at 700px 780px, #f0c9b6 0%, rgba(240,201,182,0) 100%),
      var(--mist);
  }

  .blobs { position: absolute; left: 0; top: 0; }

  .why-list {
    position: absolute; left: 27px; top: 42px; margin: 0; padding: 0; list-style: none;
    font-family: "Bebas Neue", sans-serif; font-size: 52px; line-height: 52.6px; color: var(--white);
  }
  .why-list li { padding-left: 25px; }
  .why-list li.why-heading { padding-left: 0; }

  .sliding-scale {
    position: absolute; left: 545px; top: 42px; margin: 0;
    font-family: "Bebas Neue", sans-serif; font-weight: 400; font-size: 53px; line-height: 52.6px; color: var(--ink);
  }

  .services {
    position: absolute; left: 470px; top: 400px; width: 430px; text-align: center;
    font-family: "Josefin Sans", sans-serif; font-weight: 600; color: var(--ink);
    text-transform: uppercase;
  }
  .services h2 { margin: 0; font-size: 15px; font-weight: 600; letter-spacing: 2.6px; line-height: 24px; }
  .services ul { list-style: none; margin: 0; padding: 0; font-size: 15px; letter-spacing: 2.6px; line-height: 23.7px; }
  .services .more { margin: 8px 0 0; font-size: 11.5px; letter-spacing: 1.6px; }

  .brand { position: absolute; left: 27px; top: 1000px; width: 320px; text-align: center; }
  .brand-name { font-family: "Bebas Neue", sans-serif; font-size: 34px; line-height: 36px; color: var(--ink); letter-spacing: 1px; }
  .brand-tag { font-family: "Montserrat", sans-serif; font-size: 9.5px; color: var(--ink); margin-top: 6px; }

  .contact {
    position: absolute; right: 24px; top: 1008px; width: 420px; text-align: right;
    font-family: "Josefin Sans", sans-serif; font-weight: 600; font-size: 11.5px; letter-spacing: 1.4px;
    line-height: 16px; color: var(--ink);
  }
  .contact a { color: var(--ink); text-decoration: none; }
  .website {
    position: absolute; right: 24px; top: 1044px; width: 400px; text-align: right;
    font-family: "Josefin Sans", sans-serif; font-weight: 700; font-size: 14.5px; letter-spacing: 1.8px; color: var(--ink);
    text-decoration: none; text-transform: uppercase; white-space: nowrap;
  }

  .footer { position: absolute; left: 0; top: 1093px; width: 900px; height: 107px; background: var(--white); }
  .partner-group { position: absolute; left: 60px; top: 25px; display: flex; align-items: center; gap: 10px; }
  .partner-mark { width: 46px; height: 46px; border-radius: 50%; background: var(--circle-blue); }
  .partner-name { font-family: "Montserrat", sans-serif; font-size: 13.5px; line-height: 14.5px; color: var(--footer-ink); }

  .membership { position: absolute; left: 298px; top: 18px; }
  .membership-label { font-family: "Montserrat", sans-serif; font-size: 11px; color: var(--gold); }
  .membership-row { display: flex; align-items: center; gap: 12px; margin-top: 8px; }
  .membership-badge { width: 86px; height: 30px; background: var(--olive); }
  .membership-name { font-family: "Montserrat", sans-serif; font-size: 11px; line-height: 14px; color: var(--gold); text-transform: uppercase; }

  .address {
    position: absolute; left: 620px; top: 32px; width: 250px; text-align: center;
    font-family: "EB Garamond", serif; font-size: 10.5px; line-height: 17px; color: var(--footer-ink); font-style: normal;
  }
</style>
</head>
<body>
<main class="flyer">
  <div class="hero-photo" role="img" aria-label="Photograph of two people gently holding hands against a soft pale grey background"></div>

  <svg class="blobs" width="900" height="1093" viewBox="0 0 900 1093" aria-hidden="true">
    <path class="blob-seafoam" fill="var(--seafoam)" d="M360,0 H900 V320 C840,350 740,372 640,370 C580,369 535,358 510,345 L360,0 Z"/>
    <path class="blob-sky" fill="var(--sky-blue)" d="M0,0 H365 C420,20 452,60 455,115 C456,125 470,128 490,140 C525,170 532,260 528,300 C522,400 480,480 420,520 C370,550 330,555 290,556 C265,557 255,546 240,552 C200,568 150,565 110,548 C70,535 30,518 0,512 Z"/>
  </svg>

  <ul class="why-list">
    <li class="why-heading">Why Mediation?</li>
    <li>Its Confidential</li>
    <li>To Save Time</li>
    <li>To Saves Money</li>
    <li>To Avoid Stress</li>
    <li>To Retain Control</li>
    <li>To Improve Outcome</li>
    <li>For Tailored Solutions</li>
  </ul>

  <h1 class="sliding-scale">Rates Available<br>On A Sliding Scale<br>To Better Suit<br>Your Needs</h1>

  <section class="services">
    <h2>Services Provided</h2>
    <ul>
      <li>- Divorce and Family Mediation</li>
      <li>- Business Mediation</li>
      <li>- Trading Mediation</li>
      <li>- Conflict Mediation</li>
      <li>- Distributor Mediation</li>
      <li>- Contract Negotiation Mediation</li>
      <li>- Merger Mediation</li>
      <li>- Property Mediation</li>
      <li>- Workplace Mediation</li>
      <li>- Mediation Coaching for Teams</li>
      <li>- Meeting Facilitation</li>
    </ul>
    <p class="more">Amongst many other services</p>
  </section>

  <div class="brand">
    <div class="brand-name">Teodric F. Morvantelk</div>
    <div class="brand-tag">Alternative Dispute Resolution</div>
  </div>

  <div class="contact">
    <a href="tel:+15553847290">+1.555.384.7290</a><br>
    <a href="mailto:teodric@morvantelkresolve.com">teodric@morvantelkresolve.com</a>
  </div>
  <a class="website" href="https://www.morvantelkresolve.com">www.morvantelkresolve.com</a>

  <footer class="footer">
    <div class="partner-group">
      <div class="partner-mark"></div>
      <div class="partner-name">Harborline<br>Accord<br>Circle</div>
    </div>
    <div class="membership">
      <div class="membership-label">Proud Members of</div>
      <div class="membership-row">
        <div class="membership-badge"></div>
        <div class="membership-name">Global Council of<br>Cooperative Practitioners</div>
      </div>
    </div>
    <address class="address">88 Larchmont Avenue #14, Westbrook MA 01999<br>USA</address>
  </footer>
</main>
</body>
</html>
```